" Temos como propósito desenvolver pessoas e proporcionar saúde transformando vidas e sorrisos. Acreditamos que a educação muda pessoas e essas transformam o mundo. E que a manutenção da saúde bucal é fundamental para a saúde geral e o aumento da auto-estima do indivíduo. Nosso principal serviço são os cursos de ortodontia para dentistas já formados (pós-graduação e cursos livres de ortodontia). Temos alguns outros cursos também para dentistas em outras áreas. "

```html
<!DOCTYPE html>
<html lang="pt-BR">
<head>
<meta charset="UTF-8">
<title>Lumio – Cartão de Visita</title>
<link href="https://fonts.googleapis.com/css2?family=Open+Sans:wght@400;600;700&display=swap" rel="stylesheet">
<style>
  :root {
    --navy: #2f4b5f;
    --navy-deep: #28404f;
    --wine: #7b1e3f;
    --paper: #ffffff;
    --ink: #2b3a45;
    --ink-soft: #4a5863;
    --rule: #c9ced2;
    --backdrop: #e9e9e9;
  }
  * { margin: 0; padding: 0; box-sizing: border-box; }
  html, body {
    width: 1200px; height: 1200px; overflow: hidden;
    background: var(--backdrop);
    font-family: "Open Sans", Arial, sans-serif;
  }
  .canvas { position: relative; width: 1200px; height: 1200px; }
  .card {
    position: absolute; left: 245px; width: 710px; height: 392px;
    border-radius: 24px; overflow: hidden;
    box-shadow: 0 18px 30px rgba(0,0,0,0.18);
  }
  .card--front {
    top: 149px; background: var(--navy);
    display: flex; align-items: center; justify-content: center;
  }
  .brand-name {
    color: var(--paper); font-weight: 700; letter-spacing: 1px;
    line-height: 1;
  }
  .card--front .brand-name { font-size: 128px; }
  .card--back { top: 660px; background: var(--navy); }
  .card-shapes { position: absolute; inset: 0; }
  .marker {
    position: absolute; left: 0; top: 53px; width: 55px; height: 55px;
    background: var(--navy);
  }
  .identity { position: absolute; left: 79px; top: 52px; color: var(--ink); }
  .identity .person { font-size: 29px; line-height: 1.15; }
  .identity .person b { font-weight: 700; }
  .identity .role { font-size: 17px; color: var(--ink-soft); margin-top: 2px; }
  .rule { position: absolute; left: 79px; width: 264px; height: 2px; background: var(--rule); }
  .rule--top { top: 130px; }
  .rule--bottom { top: 350px; }
  .contacts { position: absolute; left: 66px; top: 150px; list-style: none; }
  .contacts li {
    display: flex; align-items: center; gap: 14px;
    font-size: 17px; color: var(--ink); line-height: 1.15;
  }
  .contacts li + li { margin-top: 12px; }
  .contacts .icon { width: 30px; height: 30px; flex: none; }
  .card--back .brand-name {
    position: absolute; right: 36px; bottom: 44px; font-size: 46px;
  }
</style>
</head>
<body>
<main class="canvas">
  <section class="card card--front" aria-label="Frente do cartão">
    <span class="brand-name">Lumio</span>
  </section>

  <section class="card card--back" aria-label="Verso do cartão">
    <svg class="card-shapes" viewBox="0 0 710 392" preserveAspectRatio="none" aria-hidden="true">
      <path d="M0 0 H420 C520 80 510 300 375 392 H0 Z" fill="var(--wine)"/>
      <path d="M0 0 H398 C492 80 482 300 350 392 H0 Z" fill="var(--paper)"/>
    </svg>
    <div class="marker"></div>
    <div class="identity">
      <p class="person"><b>Nome</b> Sobrenome</p>
      <p class="role">Cargo - Função</p>
    </div>
    <div class="rule rule--top"></div>
    <ul class="contacts">
      <li>
        <svg class="icon" viewBox="0 0 30 30"><circle cx="15" cy="15" r="15" fill="var(--navy-deep)"/><path d="M10.5 8.5l2.5-.5 1.5 3.5-1.8 1.2a8 8 0 0 0 4.1 4.1l1.2-1.8 3.5 1.5-.5 2.5c-6 .5-11-4.5-10.5-10.5z" fill="#fff"/></svg>
        <span>11 9876-5432<br>11 9876-5432</span>
      </li>
      <li>
        <svg class="icon" viewBox="0 0 30 30"><circle cx="15" cy="15" r="15" fill="var(--navy-deep)"/><rect x="8" y="10" width="14" height="10" rx="1" fill="none" stroke="#fff" stroke-width="1.8"/><path d="M8 10l7 6 7-6" fill="none" stroke="#fff" stroke-width="1.8"/></svg>
        <span>email@email.com</span>
      </li>
      <li>
        <svg class="icon" viewBox="0 0 30 30"><circle cx="15" cy="15" r="15" fill="var(--navy-deep)"/><path d="M13 17l4-4M12 14l-2 2a2.8 2.8 0 0 0 4 4l2-2M18 16l2-2a2.8 2.8 0 0 0-4-4l-2 2" fill="none" stroke="#fff" stroke-width="1.8" stroke-linecap="round"/></svg>
        <span>www.site.com</span>
      </li>
      <li>
        <svg class="icon" viewBox="0 0 30 30"><circle cx="15" cy="15" r="15" fill="var(--navy-deep)"/><path d="M15 23s-5.5-6-5.5-9.5a5.5 5.5 0 0 1 11 0C20.5 17 15 23 15 23z" fill="#fff"/><circle cx="15" cy="13.5" r="2" fill="var(--navy-deep)"/></svg>
        <span>Endereço Completo<br>Bairro - Cidade - Estado - Cep</span>
      </li>
    </ul>
    <div class="rule rule--bottom"></div>
    <span class="brand-name">Lumio</span>
  </section>
</main>
</body>
</html>
```